Venlox - Property Management Company Listings - PSD / uncoded only

Our site simply connects property owners with property managers. I’m asking you to create 2 pages, 1 homepage and 1 page that lists of property management companies. Build with Responsive Design in mind. PSD/uncoded files only. Help us create a great site!
Example competitor sites:
http://www.everyestatehelp.example/
http://www.tendyourlots.example/
Inspired by these sites:
http://www.quorvik.example/
http://www.bespokely.example/
http://www.coinwire.example/
https://www.tripboard.example/
I've attached the logo as well as 2 picture files that you can consider using.
• Venlox Logo Colors: Yellow: HTML code: #FBC30A, RGB code: R: 251 G: 195 B: 10 Grey: HTML code: #4E4C4D, RGB code: R: 78 G: 76 B: 77
• The picture files are optional.
o One picture is of houses and neighborhood.
o The other is of a professional woman on the phone. Please do not use the professional woman as a large primary image. You can use the professional woman photo as a smaller photo and not the main photo.
• Please bring your own pictures and graphics too. Don't feel like you need to use mine.
Thank you!

```html
<!DOCTYPE html>
<html lang="en">
<head>
<meta charset="utf-8">
<title>Venlox – Find Your Local Property Manager</title>
<link href="https://fonts.googleapis.com/css2?family=Open+Sans:wght@300;400;600;700&display=swap" rel="stylesheet">
<style>
  :root {
    --yellow: #fbc30a;
    --grey: #4e4c4d;
    --ink: #222222;
    --text: #444444;
    --band: #2b2b2b;
    --footer: #474747;
    --footer-text: #cfcfcf;
    --white: #ffffff;
    --rule: #e3e3e3;
  }
  * { box-sizing: border-box; margin: 0; padding: 0; }
  html, body { width: 938px; height: 1200px; overflow: hidden; background: var(--white); }
  body { position: relative; font-family: "Open Sans", Arial, sans-serif; color: var(--text); }
  .abs { position: absolute; }

  /* header */
  .site-header { position: absolute; left: 0; top: 0; width: 938px; height: 62px; background: var(--white); }
  .brand { position: absolute; left: 135px; top: 14px; display: flex; align-items: center; gap: 6px; }
  .brand-mark { width: 12px; height: 12px; background: var(--yellow); }
  .brand-name { font-family: "Open Sans", sans-serif; font-weight: 700; font-size: 27px; color: var(--grey); letter-spacing: -0.5px; line-height: 1; }
  .main-nav { position: absolute; left: 465px; top: 0; height: 62px; display: flex; border-left: 1px solid var(--rule); }
  .main-nav a { display: flex; align-items: center; justify-content: center; height: 62px; border-right: 1px solid var(--rule);
    font-family: Arial, Helvetica, sans-serif; font-size: 10px; color: #555; text-decoration: none; }
  .nav-home { width: 66px; }
  .nav-manager { width: 178px; }
  .nav-contact { width: 94px; }

  /* hero */
  .hero { position: absolute; left: 0; top: 62px; width: 938px; height: 406px;
    background: linear-gradient(180deg, #6f7a78 0%, #5d6a5a 35%, #4f5b47 60%, #3c4340 100%); }
  .hero-shade { position: absolute; left: 0; bottom: 0; width: 938px; height: 150px; background: linear-gradient(180deg, rgba(30,30,30,0) 0%, rgba(30,30,30,0.55) 100%); }
  .search-label { position: absolute; left: 135px; top: 289px; width: 150px; font-size: 10.5px; font-weight: 600; color: var(--white); line-height: 15px; text-transform: uppercase; }
  .field { position: absolute; top: 290px; height: 25px; background: var(--white); font-size: 6.5px; color: #555; text-transform: uppercase; padding-left: 10px; display: flex; align-items: center; }
  .field-type { left: 289px; width: 175px; }
  .field-zip { left: 476px; width: 175px; }
  .select-arrow { position: absolute; right: 6px; top: 7px; width: 11px; height: 11px; border: 1px solid #999; }
  .select-arrow::after { content: ""; position: absolute; left: 2px; top: 3px; border-left: 3px solid transparent; border-right: 3px solid transparent; border-top: 4px solid #555; }
  .btn-search { position: absolute; left: 662px; top: 290px; width: 96px; height: 26px; background: var(--yellow); border-bottom: 2px solid #d9a600;
    font-size: 9.5px; font-weight: 600; color: var(--ink); display: flex; align-items: center; justify-content: center; text-transform: uppercase; }
  .hero-rule { position: absolute; left: 135px; top: 336px; width: 669px; height: 1px; background: rgba(255,255,255,0.85); }
  .hero-tagline { position: absolute; left: 135px; top: 355px; width: 669px; text-align: center; font-size: 10.5px; color: var(--white); text-transform: uppercase; }

  /* steps */
  .section-title { position: absolute; left: 0; top: 525px; width: 938px; text-align: center; font-size: 17.5px; font-weight: 600; color: var(--ink); text-transform: uppercase; }
  .step { position: absolute; top: 588px; width: 220px; text-align: center; }
  .step-icon { width: 120px; height: 120px; border-radius: 50%; background: var(--yellow); margin: 0 auto; display: flex; align-items: center; justify-content: center; }
  .step-text { margin-top: 17px; font-size: 10.5px; font-weight: 300; color: #333; line-height: 18px; text-transform: uppercase; }
  .step-1 { left: 127px; }
  .step-2 { left: 348px; }
  .step-3 { left: 588px; }

  /* feature cards */
  .feature { position: absolute; top: 808px; width: 210px; }
  .feature-photo { width: 210px; height: 123px; }
  .feature-text { margin-top: 9px; font-size: 9.5px; color: var(--ink); line-height: 18px; padding-left: 1px; }
  .feature-1 { left: 134px; }
  .feature-1 .feature-photo { background: linear-gradient(180deg, #3b73b8 0%, #d9d3c2 45%, #ece6d8 80%, #6fb3c9 100%); }
  .feature-2 { left: 365px; }
  .feature-2 .feature-photo { background: linear-gradient(90deg, #c9cbc6 0%, #e4e3df 55%, #b9bab5 100%); }
  .feature-3 { left: 595px; }
  .feature-3 .feature-photo { background: linear-gradient(135deg, #b7bfae 0%, #e6dccb 45%, #c9a88b 70%, #2e3a55 100%); }

  /* manager band */
  .manager-band { position: absolute; left: 0; top: 1018px; width: 938px; height: 102px; background: var(--band); }
  .band-title { position: absolute; left: 135px; top: 16px; font-size: 19px; font-weight: 600; color: var(--white); }
  .band-text { position: absolute; left: 135px; top: 47px; width: 540px; font-size: 9.5px; color: #bdbdbd; line-height: 18px; }
  .btn-learn { position: absolute; left: 685px; top: 39px; width: 118px; height: 38px; background: var(--yellow); border-bottom: 2px solid #d9a600;
    font-size: 11px; font-weight: 600; color: var(--ink); display: flex; align-items: center; justify-content: center; text-transform: uppercase; }

  /* footer */
  .site-footer { position: absolute; left: 0; top: 1120px; width: 938px; height: 80px; background: var(--footer); }
  .footer-links { position: absolute; left: 135px; top: 24px; font-family: Arial, Helvetica, sans-serif; font-size: 7.5px; color: var(--footer-text); }
  .footer-links span.sep { margin: 0 9px; }
  .copyright { position: absolute; left: 135px; top: 48px; font-family: Arial, Helvetica, sans-serif; font-size: 7.5px; color: var(--footer-text); }
  .social { position: absolute; top: 25px; width: 27px; height: 27px; border-radius: 50%; border: 1.5px solid #9a9a9a; }
  .social-1 { left: 677px; }
  .social-2 { left: 710px; }
  .social-3 { left: 743px; }
  .social-4 { left: 777px; }
</style>
</head>
<body>
  <header class="site-header">
    <div class="brand"><span class="brand-mark"></span><span class="brand-name">Venlox</span></div>
    <nav class="main-nav">
      <a class="nav-home" href="#">Home</a>
      <a class="nav-manager" href="#">Are you a Property Manager?</a>
      <a class="nav-contact" href="#">Contact Us</a>
    </nav>
  </header>

  <section class="hero">
    <div class="abs" style="left:0;top:0;width:938px;height:406px;" role="img" aria-label="Aerial photo of a suburban neighbourhood with two-storey houses, lawns and trees"></div>
    <div class="hero-shade"></div>
    <div class="search-label">Find your local property manager</div>
    <div class="field field-type">Select your property type<span class="select-arrow"></span></div>
    <div class="field field-zip">In zipcode</div>
    <div class="btn-search">Search now</div>
    <div class="hero-rule"></div>
    <p class="hero-tagline">Search our directory to find experienced and professional property management companies that meet your needs.</p>
  </section>

  <h2 class="section-title">To find property management companies near you:</h2>

  <div class="step step-1">
    <div class="step-icon">
      <svg width="64" height="64" viewBox="0 0 64 64" aria-hidden="true">
        <path d="M12 14 Q32 4 52 14 L48 18 Q32 10 16 18 Z" fill="#4e4c4d"/>
        <path d="M32 18 L14 32 L18 32 L18 48 L46 48 L46 32 L50 32 Z" fill="#4e4c4d"/>
        <rect x="27" y="34" width="10" height="14" fill="#fbc30a"/>
        <rect x="29" y="36" width="6" height="8" fill="#4e4c4d"/>
        <path d="M10 46 Q32 64 54 46 L52 52 Q32 66 12 52 Z" fill="#4e4c4d"/>
      </svg>
    </div>
    <p class="step-text">Select your property type<br>and zipcode</p>
  </div>

  <div class="step step-2">
    <div class="step-icon">
      <svg width="64" height="64" viewBox="0 0 64 64" aria-hidden="true">
        <path d="M6 34 L18 28 L30 34 L44 22 L58 16 L58 54 L6 54 Z" fill="#4e4c4d"/>
        <path d="M6 30 L18 22 L30 28 L50 12" stroke="#4e4c4d" stroke-width="3" fill="none"/>
        <path d="M44 10 L54 8 L52 18 Z" fill="#4e4c4d"/>
        <rect x="17" y="30" width="2" height="24" fill="#fbc30a"/>
        <rect x="30" y="34" width="2" height="20" fill="#fbc30a"/>
        <rect x="43" y="24" width="2" height="30" fill="#fbc30a"/>
      </svg>
    </div>
    <p class="step-text">Review property manager listings<br>in your area</p>
  </div>

  <div class="step step-3">
    <div class="step-icon">
      <svg width="64" height="64" viewBox="0 0 64 64" aria-hidden="true">
        <path d="M12 16 Q32 2 52 16 L48 20 Q32 10 16 20 Z" fill="#4e4c4d"/>
        <circle cx="20" cy="26" r="5" fill="#4e4c4d"/>
        <circle cx="44" cy="26" r="5" fill="#4e4c4d"/>
        <circle cx="32" cy="24" r="6" fill="#4e4c4d"/>
        <rect x="13" y="32" width="14" height="14" rx="3" fill="#4e4c4d"/>
        <rect x="37" y="32" width="14" height="14" rx="3" fill="#4e4c4d"/>
        <rect x="24" y="31" width="16" height="17" rx="3" fill="#4e4c4d" stroke="#fbc30a" stroke-width="1.5"/>
        <rect x="16" y="46" width="3" height="10" fill="#4e4c4d"/>
        <rect x="21" y="46" width="3" height="10" fill="#4e4c4d"/>
        <rect x="40" y="46" width="3" height="10" fill="#4e4c4d"/>
        <rect x="45" y="46" width="3" height="10" fill="#4e4c4d"/>
        <rect x="27" y="48" width="4" height="10" fill="#4e4c4d"/>
        <rect x="33" y="48" width="4" height="10" fill="#4e4c4d"/>
      </svg>
    </div>
    <p class="step-text">Select and compare property<br>managers</p>
  </div>

  <article class="feature feature-1">
    <div class="feature-photo" role="img" aria-label="Photo of a large white villa with a terracotta roof and a swimming pool"></div>
    <p class="feature-text">Making renting YOUR home an easy,<br>stress-free experience.</p>
  </article>
  <article class="feature feature-2">
    <div class="feature-photo" role="img" aria-label="Photo of a professional businesswoman talking on a phone in an office corridor"></div>
    <p class="feature-text">Connecting property owners with property<br>managers.</p>
  </article>
  <article class="feature feature-3">
    <div class="feature-photo" role="img" aria-label="Photo of a hand holding a small model house in front of a blurred home"></div>
    <p class="feature-text">Providing property management solutions,<br>simplified.</p>
  </article>

  <section class="manager-band">
    <h3 class="band-title">Are you a Property Manager?</h3>
    <p class="band-text">Join our real estate property management company network. Let us help you find leads of property owners seeking to rent their homes.</p>
    <div class="btn-learn">Learn more</div>
  </section>

  <footer class="site-footer">
    <div class="footer-links">Are you a Property Manager?<span class="sep">/</span>About Us<span class="sep">/</span>Contact Us<span class="sep">/</span>Terms of Use<span class="sep">/</span>Privacy Policy<span class="sep">/</span>Site Map</div>
    <div class="copyright">Copyright © 2014, Venlox, All Rights Reserved</div>
    <span class="social social-1"></span>
    <span class="social social-2"></span>
    <span class="social social-3"></span>
    <span class="social social-4"></span>
  </footer>
</body>
</html>
```